In Home Personal IT Consultant (Nerd) Website and Logo LOpalo.com

Website and logo design for in home personal "nerd". Consulting services provided: Home Automation, Home Theater, Network and Wi-Fi installation, Computer Repair, and Virus Removal. Need simple site to promote LOpalo.com based in Santa Fe, New Mexico. You may choose to incorporate the Zia symbol from the New Mexico flag into the design, not mandatory. I am also a big fan of the movie Summer at Crane Lake.
I have over 10 years of experience in the hospitality industry working with multi million dollar hotels and will apply that same level of service to the home. Veltrona K7 and Bulwark+ Certified. Available by appointment, primarily Evenings and Weekends. Consulting rate will be $70/hr.
Consulting
1 page

```html
<!DOCTYPE html>
<html lang="en">
<head>
<meta charset="utf-8">
<title>Lopalo Consulting Services</title>
<link rel="stylesheet" href="https://fonts.googleapis.com/css2?family=Open+Sans:ital,wght@0,300;0,400;0,600;0,700;1,400&display=swap">
<style>
:root{
  --teal:#2fd0d6;
  --teal-soft:#74cfcc;
  --ink:#333;
  --muted:#777;
  --page:#f3f3f3;
  --band:#e9e9e9;
  --footer:#242424;
  --footer-base:#1b1b1b;
  --header:rgba(38,34,36,.92);
}
*{margin:0;padding:0;box-sizing:border-box}
html,body{width:1200px;height:1200px;overflow:hidden;background:#000}
body{font-family:'Open Sans',sans-serif;color:var(--ink)}
.page{position:absolute;left:275px;top:0;width:813px;height:1500px;transform:scale(.8);transform-origin:0 0;background:var(--page);overflow:hidden}
.abs{position:absolute}

/* header */
.site-header{left:0;top:0;width:813px;height:37px;background:var(--header);z-index:3}
.brand{left:101px;top:6px;color:var(--teal);font-weight:700;font-size:14px;letter-spacing:4px}
.brand-tag{left:101px;top:24px;color:#ccc;font-size:4.5px}
.nav{left:563px;top:19px;display:flex;gap:13px;font-size:8px;color:#ddd}
.nav span.active{border-bottom:1px solid var(--teal);padding-bottom:10px}

/* hero */
.hero{left:0;top:0;width:813px;height:371px;background:radial-gradient(ellipse at 30% 60%,#8d7f80 0%,#5e5052 45%,#3e3436 100%)}
.hero-tablet{left:77px;top:135px;width:248px;height:194px;border-radius:8px;background:linear-gradient(135deg,#2a2a2a,#111)}
.hero-kicker{left:416px;top:134px;color:#fff;font-size:19px;font-weight:300}
.hero-title{left:416px;top:155px;color:var(--teal);font-size:31px;font-weight:600;letter-spacing:-.5px}
.hero-copy{left:417px;top:200px;color:#fff;font-size:8.6px;line-height:13.5px}
.btn-pill{background:var(--teal);color:#fff;font-size:8.5px;font-weight:600;border-radius:12px;display:flex;align-items:center;justify-content:center}
.hero-btn{left:417px;top:247px;width:79px;height:21px}
.dots{left:701px;top:178px;width:15px;height:52px;background:rgba(40,40,40,.5);border-radius:8px;display:flex;flex-direction:column;align-items:center;justify-content:space-around;padding:3px 0}
.dots i{width:5px;height:5px;border-radius:50%;border:1px solid #fff}
.dots i.on{background:#fff}

/* about */
.about-label{left:103px;top:415px;font-size:17px;font-weight:300}
.about-title{left:103px;top:430px;font-size:46px;font-weight:700;color:var(--teal);letter-spacing:1px}
.about-lead{left:107px;top:491px;width:240px;font-size:7px;font-weight:700;line-height:11px;color:#222}
.about-body{left:107px;top:520px;width:240px;font-size:6.8px;line-height:11.2px;color:var(--muted)}
.about-btn{left:107px;top:582px;width:78px;height:21px}
.about-photo{left:406px;top:420px;width:306px;height:182px;background:linear-gradient(135deg,#5d7078,#b7c2c4 55%,#e3e6e6)}

/* services */
.services{left:0;top:650px;width:813px;height:318px;background:var(--band)}
.section-title{width:813px;text-align:center;font-size:17px;font-weight:300;color:#333}
.section-title b{color:var(--teal);font-weight:700}
.services .section-title{top:12px;left:0}
.grid{left:102px;top:46px;width:612px;height:210px;display:grid;grid-template-columns:repeat(4,153px);grid-template-rows:105px 105px}
.tile-photo{width:153px;height:105px}
.tile-text{background:#fff;padding:17px 15px 0;position:relative}
.tile-text h3{color:var(--teal);font-size:8.3px;font-weight:600;line-height:9px;margin-bottom:7px}
.tile-text p{font-size:6.4px;line-height:10px;color:#777}
.tile-text .more{color:var(--teal);font-size:6.8px;margin-top:7px;display:block}
.tile-text.left::before,.tile-text.right::after{content:"";position:absolute;top:46px;border:6px solid transparent}
.tile-text.left::before{left:-12px;border-right-color:#fff}
.tile-text.right::after{right:-12px;border-left-color:#fff}
.view-all{left:333px;top:273px;width:147px;height:23px;background:var(--teal);color:#fff;font-size:10.5px;font-weight:600;display:flex;align-items:center;justify-content:center}

/* testimonials */
.testimonials{left:0;top:968px;width:813px;height:292px;background:#f4f4f4}
.testimonials .section-title{top:40px;left:0}
.quote{top:84px;width:193px;height:108px;background:var(--teal-soft);color:#fff}
.quote p{position:absolute;left:27px;top:27px;width:150px;font-size:7px;line-height:10.6px;font-weight:300}
.quote .sig{position:absolute;right:26px;top:76px;font-size:7.5px;font-style:italic;font-family:Georgia,serif;color:#3f8d8a}
.qmark{position:absolute;font-family:Georgia,serif;font-size:38px;font-weight:700;color:#4eaeab;line-height:1}
.qmark.open{left:4px;top:10px}
.qmark.close{right:4px;top:64px}
.avatar{position:absolute;left:2px;top:90px;width:36px;height:36px;border-radius:50%;border:2px solid #fff;background:linear-gradient(#c9b8aa,#8e7f76)}
.pager{left:388px;top:242px;display:flex;gap:3px}
.pager span{width:17px;height:17px;background:#ccc;display:flex;align-items:center;justify-content:center}

/* footer */
.site-footer{left:0;top:1260px;width:813px;height:208px;background:var(--footer);color:#fff}
.col-title{font-size:8.5px;font-weight:600}
.contact-list{left:102px;top:66px;font-size:6.8px;color:#999;line-height:15.4px}
.contact-list div{display:flex;align-items:center;gap:6px}
.sitemap{left:290px;top:66px;font-size:6.8px;color:#999;line-height:16.2px}
.sitemap span::before{content:"";display:inline-block;width:4px;height:4px;background:var(--teal);margin-right:5px;vertical-align:middle}
.field{font-size:6.8px;color:#fff;border-bottom:1px solid #777;height:13px}
.send{left:651px;top:149px;width:61px;height:20px;background:var(--teal-soft);color:#1d1d1d;font-size:9px;display:flex;align-items:center;justify-content:center}
.to-top{left:772px;top:1452px;width:28px;height:16px;background:#2e2e2e}
.footer-base{left:0;top:1468px;width:813px;height:32px;background:var(--footer-base)}
.copyright{left:0;top:11px;width:813px;text-align:center;font-size:6.8px;color:#555}
.socials{left:646px;top:11px;display:flex;gap:8px}
.socials i{width:9px;height:9px;border-radius:50%;background:#777}
</style>
</head>
<body>
<div class="page">

  <section class="hero abs" role="img" aria-label="Blurred living room with hands holding a tablet showing a home security app"></section>
  <div class="hero-tablet abs" role="img" aria-label="Tablet displaying a room view with a lock icon"></div>
  <div class="hero-kicker abs">Secure Your Home use to</div>
  <div class="hero-title abs">Home Automation</div>
  <p class="hero-copy abs">Lorem ipsum dolor sit amet, consectetur adipiscing elit.<br>Phasellus suscipit pulvinar metussit amet</p>
  <div class="hero-btn btn-pill abs">Read More</div>
  <div class="dots abs"><i class="on"></i><i></i><i></i><i></i></div>

  <header class="site-header abs">
    <div class="brand abs">LOPALO</div>
    <div class="brand-tag abs">Consulting Services Provided</div>
    <nav class="nav abs"><span class="active">Home</span><span>About</span><span>Services</span><span>Contact Us</span></nav>
  </header>

  <div class="about-label abs">About</div>
  <div class="about-title abs">LOPALO</div>
  <p class="about-lead abs">Lorem ipsum dolor sit amet, consectetur adipiscing elit. Phasellus suscipit pulvinar metus,</p>
  <p class="about-body abs">Sit amet pulvinar diam accumsan in. Nullam ac nunc id orci pulvinar vehicula sit amet et ligula. Etiam posuere suscipit tempus. Quisque sed accumsan est, non ornare ante. Interdum et malesuada fames ac ante ipsum primis in faucibus.</p>
  <div class="about-btn btn-pill abs">Read More</div>
  <div class="about-photo abs" role="img" aria-label="Two people working over notes beside laptops"></div>

  <section class="services abs">
    <h2 class="section-title abs">OUR <b>SERVICES</b></h2>
    <div class="grid abs">
      <div class="tile-photo" role="img" aria-label="Hand adjusting a wall thermostat" style="background:linear-gradient(135deg,#efece8,#cfc6bd)"></div>
      <div class="tile-text left"><h3>Home Automation</h3><p>Donec a quam at ipsum luctus semper. Fusce sodales, tortor et porttitor aliquet, tortor sapien venenatis massa.</p><span class="more">Read More ▸</span></div>
      <div class="tile-photo" role="img" aria-label="Home theater room with projection screen" style="background:linear-gradient(#e6e6e6,#a9a9a9 60%,#3a3a3a)"></div>
      <div class="tile-text left"><h3>Home Theater</h3><p>Donec a quam at ipsum luctus semper. Fusce sodales, tortor et porttitor aliquet, tortor sapien venenatis massa.</p><span class="more">Read More ▸</span></div>
      <div class="tile-text right" style="padding-left:24px"><h3>Network and<br>Wi-Fi installation</h3><p>Donec a quam at ipsum luctus semper. Fusce sodales, tortor et porttitor aliquet, tortor</p><span class="more">Read More ▸</span></div>
      <div class="tile-photo" role="img" aria-label="Technician mounting a wireless router on a wall" style="background:linear-gradient(135deg,#f0f0f0,#c8c8c8 55%,#3b3430)"></div>
      <div class="tile-text right" style="padding-left:22px"><h3>Computer Repair</h3><p>Donec a quam at ipsum luctus semper. Fusce sodales, tortor et porttitor aliquet, tortor sapien venenatis massa.</p><span class="more">Read More ▸</span></div>
      <div class="tile-photo" role="img" aria-label="Close-up of a circuit board being repaired" style="background:linear-gradient(135deg,#e8ecea,#6f8a7d 55%,#2f9a5a)"></div>
    </div>
    <div class="view-all abs">View All Services</div>
  </section>

  <section class="testimonials abs">
    <h2 class="section-title abs">CLIENT <b>TESTIMONIALS</b></h2>
    <div class="quote abs" style="left:102px"><span class="qmark open">“</span><p>Nulla commodo tellus non mauris mattis condimentum. Mauris feugiat lorem amet pharetra lacinia. Morbi tincidunt rhoncus posuere. Etiam at arcu in augue.</p><span class="sig">-Lorem ipsum</span><span class="qmark close">”</span><div class="avatar" role="img" aria-label="Client portrait"></div></div>
    <div class="quote abs" style="left:310px"><span class="qmark open">“</span><p>Nulla commodo tellus non mauris mattis condimentum. Mauris feugiat lorem amet pharetra lacinia. Morbi tincidunt rhoncus posuere. Etiam at arcu in augue.</p><span class="sig">-Lorem ipsum</span><span class="qmark close">”</span><div class="avatar" role="img" aria-label="Client portrait"></div></div>
    <div class="quote abs" style="left:518px"><span class="qmark open">“</span><p>Nulla commodo tellus non mauris mattis condimentum. Mauris feugiat lorem amet pharetra lacinia. Morbi tincidunt rhoncus posuere. Etiam at arcu in augue.</p><span class="sig">-Lorem ipsum</span><span class="qmark close">”</span><div class="avatar" role="img" aria-label="Client portrait"></div></div>
    <div class="pager abs">
      <span><svg width="8" height="10"><path d="M6 1 2 5l4 4" fill="none" stroke="#555" stroke-width="1"/></svg></span>
      <span><svg width="8" height="10"><path d="M2 1l4 4-4 4" fill="none" stroke="#555" stroke-width="1"/></svg></span>
    </div>
  </section>

  <footer class="site-footer abs">
    <div class="col-title abs" style="left:102px;top:43px">Contact Us</div>
    <div class="contact-list abs">
      <div><svg width="7" height="9"><path d="M3.5 0a3 3 0 0 1 3 3c0 2-3 6-3 6s-3-4-3-6a3 3 0 0 1 3-3z" fill="#2fd0d6"/></svg>45 BC, making it over 2000</div>
      <div><svg width="7" height="7"><path d="M1 0h2l1 2-1 1q1 2 2 2l1-1 1 1v2h-1Q1 7 0 1z" fill="#2fd0d6"/></svg>01-555-017-246</div>
      <div><svg width="7" height="6"><rect x=".5" y=".5" width="6" height="5" fill="none" stroke="#2fd0d6"/><path d="M.5.5l3 3 3-3" fill="none" stroke="#2fd0d6"/></svg>info@lopaloconsulting.com</div>
      <div><svg width="7" height="7"><circle cx="3.5" cy="3.5" r="3" fill="none" stroke="#2fd0d6"/><path d="M.5 3.5h6M3.5.5v6" stroke="#2fd0d6"/></svg>www.lopaloconsulting.com</div>
    </div>
    <div class="col-title abs" style="left:290px;top:43px">Sitemap</div>
    <div class="sitemap abs"><span>Home</span><br><span>About</span><br><span>Services</span><br><span>Contact Us</span></div>
    <div class="col-title abs" style="left:408px;top:43px">Get In Touch</div>
    <div class="field abs" style="left:408px;top:67px;width:147px">First Name :</div>
    <div class="field abs" style="left:567px;top:67px;width:145px">Last Name :</div>
    <div class="field abs" style="left:408px;top:92px;width:147px">Email:</div>
    <div class="field abs" style="left:567px;top:92px;width:145px">Phone:</div>
    <div class="field abs" style="left:408px;top:118px;width:304px">Comment:</div>
    <div class="send abs">SEND</div>
  </footer>
  <div class="to-top abs"><svg width="28" height="16"><path d="M10 10l4-4 4 4" fill="none" stroke="#aaa"/></svg></div>
  <div class="footer-base abs">
    <div class="copyright abs">© 2017 Lopalo Consulting Services. All Right Reserved.</div>
    <div class="socials abs"><i></i><i></i><i></i><i></i></div>
  </div>
</div>
</body>
</html>
```